■デザインへの要望
1)フライヤーのイメージとしては明るく女性的なイメージを希望します。
2)人物写真は使わないでください。
3)コーポレートロゴを右上に配置してください。
ロゴの改変(色の変更や比率の変更)はご遠慮ください。
4)会のロゴを配置してください。
位置はお任せしますが、サイズの変更はご遠慮ください。
※前回のフライヤーを素材と一緒にお付けしますのでご参考になさってください。

■素材
1)フライヤーを作成する際に必要なロゴ等の画像等は

```html
<!DOCTYPE html>
<html lang="ja">
<head>
<meta charset="UTF-8">
<title>ランチョンセミナー15 フライヤー</title>
<link rel="stylesheet" href="https://fonts.googleapis.com/css2?family=Noto+Sans+JP:wght@400;500;700;900&family=Noto+Serif+JP:wght@500;700;900&display=swap">
<style>
  :root {
    --red: #c8161e;
    --red-deep: #b01018;
    --ink: #2a1a12;
    --white: #ffffff;
  }
  * { margin: 0; padding: 0; box-sizing: border-box; }
  html, body { width: 851px; height: 1200px; overflow: hidden; }
  body { font-family: "Noto Sans JP", sans-serif; color: var(--ink); }
  .flyer {
    position: relative; width: 851px; height: 1200px; overflow: hidden;
    background:
      radial-gradient(ellipse 62% 46% at 50% 46%, rgba(255,255,255,0.96) 0%, rgba(255,255,255,0.7) 45%, rgba(255,255,255,0) 75%),
      radial-gradient(circle at 14% 18%, rgba(255,255,255,0.55) 0, rgba(255,255,255,0) 80px),
      radial-gradient(circle at 86% 70%, rgba(255,255,255,0.5) 0, rgba(255,255,255,0) 110px),
      radial-gradient(circle at 10% 86%, rgba(255,255,255,0.45) 0, rgba(255,255,255,0) 120px),
      linear-gradient(160deg, #ffe45a 0%, #fff3a8 40%, #ffe77a 75%, #f8cf2c 100%);
  }
  .society-mark { position: absolute; left: 48px; top: 112px; display: flex; align-items: center; gap: 8px; font-weight: 700; font-size: 20px; color: var(--ink); }
  .society-mark .square { width: 22px; height: 22px; background: var(--red); }
  .sponsor-mark { position: absolute; right: 40px; top: 34px; font-weight: 700; font-size: 26px; color: var(--ink); }
  .congress { position: absolute; top: 112px; left: 0; width: 100%; text-align: center; font-family: "Noto Serif JP", serif; font-weight: 700; }
  .congress .edition { font-size: 28px; line-height: 1.3; }
  .congress .name { font-size: 30px; line-height: 1.3; }
  .seminar { position: absolute; top: 218px; left: 0; width: 100%; text-align: center; font-size: 30px; font-weight: 700; line-height: 46px; }
  .title { position: absolute; top: 266px; left: 0; width: 100%; text-align: center; color: var(--red); font-weight: 900; }
  .title .line { font-size: 47px; line-height: 49px; display: block; }
  .title .sub { font-size: 45px; line-height: 49px; display: block; letter-spacing: -0.02em; }
  .title-en { position: absolute; top: 412px; width: 100%; text-align: center; font-size: 21px; color: var(--red-deep); font-family: Arial, "Noto Sans JP", sans-serif; }
  .date { position: absolute; top: 458px; width: 100%; text-align: center; color: var(--red); font-weight: 900; font-size: 48px; line-height: 60px; font-family: "Noto Serif JP", serif; }
  .date .small { font-size: 28px; }
  .date .wd { display: inline-block; width: 30px; height: 30px; border-radius: 50%; background: var(--red); color: var(--white); font-size: 18px; line-height: 30px; vertical-align: 6px; margin: 0 4px; font-family: "Noto Sans JP", sans-serif; }
  .venue { position: absolute; top: 514px; width: 100%; text-align: center; font-family: "Noto Serif JP", serif; font-weight: 700; font-size: 24px; line-height: 36px; }
  .person { position: absolute; left: 120px; display: flex; align-items: flex-start; gap: 30px; }
  .person.chair { top: 694px; }
  .person.speaker { top: 778px; }
  .role { width: 52px; height: 52px; margin-top: 4px; background: var(--red); color: var(--white); font-weight: 700; font-size: 19px; display: flex; align-items: center; justify-content: center; border-radius: 4px; }
  .person .name { font-family: "Noto Serif JP", serif; font-weight: 700; font-size: 42px; line-height: 56px; letter-spacing: 0.1em; }
  .person .name small { font-size: 24px; letter-spacing: 0; margin-left: 80px; }
  .affil { font-size: 13px; line-height: 1.6; }
  .person.chair .affil { position: absolute; left: 280px; top: 58px; white-space: nowrap; }
  .cohost { position: absolute; top: 1108px; width: 100%; text-align: center; font-size: 15px; line-height: 1.7; font-weight: 500; }
</style>
</head>
<body>
  <div class="flyer">
    <div class="society-mark"><span class="square"></span>JSCN</div>
    <div class="sponsor-mark">ミライケア</div>

    <header class="congress">
      <div class="edition">第25回</div>
      <div class="name">日本嚥下ケア看護学会学術大会</div>
    </header>

    <div class="seminar">ランチョンセミナー15</div>

    <h1 class="title">
      <span class="line">これからの摂食嚥下障害看護に</span>
      <span class="line">何が求められているか</span>
      <span class="sub">〜「機能低下予防」と「終末期care」〜</span>
    </h1>
    <p class="title-en">What is required in the future for dysphagia nursing</p>

    <p class="date">2019<span class="small">年</span>9<span class="small">月</span>7<span class="small">日</span><span class="wd">土</span>12:00-13:00</p>

    <div class="venue">
      <div>第8会場</div>
      <div>潮風メッセ新港コンベンションセンター2F</div>
      <div>中会議室201</div>
    </div>

    <div class="person chair">
      <div class="role">座長</div>
      <div class="name">高森　綾乃<small>先生</small></div>
      <p class="affil">みなと看護大学　名誉教授</p>
    </div>

    <div class="person speaker">
      <div class="role">演者</div>
      <div>
        <div class="name">岡野　美月<small>先生</small></div>
        <p class="affil">公益社団法人東海県看護協会　認定看護師教育課程専任教員<br>摂食・嚥下障害看護認定看護師教育課程　主任教員</p>
      </div>
    </div>

    <footer class="cohost">
      共催：第25回日本嚥下ケア看護学会学術大会<br>ミライケア株式会社
    </footer>
  </div>
</body>
</html>
```